Harbor Motor Website

We need a Wordpress site designed for a local automotive repair facility. Our goals for the website are the following:
-"Humanize" the business by showing our people and location (building).
-Communicate our "Local / Community" orientation (not a national chain store)
-Above the fold call to action(s). Online Appointment Schedule, Loaner Car Reservation and Chat Feature.
-Business Strengthening by showing industry affiliations.
Our corporate colors are: Blue Pantone 293 and Light Grey 427. Accent colors are Yellow Pantone 123 and Lime Green (lots of colors i know)
We have been trying to develop a site similar to this site: www.brightlanegarage.com. I like the header image(s). I believe this site reinforces local ownership and conveys trust.
We built this site to try and duplicate but I do not like the results:
http://pelvistudio.com/harbor2/
This is our current site: www.harbormotorrepairplace.com
My SEO firm would like you to adhere to the following:
Here are the basics:
+ Full width of site 1080px, centered
+ Header no taller than 300px
+ Need standard selection of pages, including a full page layout
+ On pages with a sidebar, main column width at least 640px, sidebar 320px
+ All page titles should be an H1, and the only H1 on the page
+ Provide 4 footer widgets spanning the width of the site
Images are uploaded. Please let me know if there are additional images or direction needed.
Thanks,
Martin Kovacs
I have made committed on the payment for this project. I am looking forward to seeing some great WordPress designs.
Thank you,
Martin
I have uploaded an image of a Postcard that we send out in our local area. Many of our print materials carry this type of look and feel.
I HESITATED to upload this because I do not want to "stifle" or "steer" your creativity. I thought you may be able to pull some elements out of this for consistency. It is alright if you choose a different direction with your graphic elements.
Thanks,
Martin
First off, thanks for all the great work. Make sure you get your final ideas uploaded by the deadline (tomorrow).
I will take a few days to review, get feedback from my colleges and then make a final selection.
Your hard work is appreciated.
Sincerely,
Martin
Target Market(s)
35-60 years old with an even mix of male and female.
Upper income demographic who are driving 2+ vehicles in the household that are 3 years or older.
Industry/Entity Type
Automotive
Look and feel

```html
<!DOCTYPE html>
<html lang="en">
<head>
<meta charset="utf-8">
<title>Harbor Motor Repair</title>
<link href="https://fonts.googleapis.com/css2?family=Mulish:wght@400;600;700&family=Libre+Baskerville:wght@400&display=swap" rel="stylesheet">
<style>
:root{
  --blue-deep:#0b3f8f;
  --blue:#1a5fc4;
  --blue-bright:#2f7de0;
  --side:#e3f0fb;
  --text:#333;
  --grey:#8a8a8a;
  --yellow:#f6c31a;
  --star:#f5a623;
}
*{box-sizing:border-box;margin:0;padding:0}
html,body{width:800px;height:1200px;overflow:hidden}
body{position:relative;font-family:"Mulish",sans-serif;color:var(--text);
  background:linear-gradient(180deg,#c4def4 0,#7fb2e8 120px,#2a6cc8 360px,#0e4aa6 800px,#1457b5 1200px)}
.abs{position:absolute}
/* header */
.shop-photo{left:290px;top:24px;width:270px;height:151px;
  background:linear-gradient(180deg,#d9e6f2 0,#e6d6b8 22%,#c9a878 40%,#8a7460 62%,#b9b0a2 85%,#cfd8e2 100%);
  -webkit-mask-image:linear-gradient(90deg,transparent 0,#000 18%,#000 82%,transparent 100%);
  mask-image:linear-gradient(90deg,transparent 0,#000 18%,#000 82%,transparent 100%);opacity:.85}
.owner-photo{left:122px;top:6px;width:124px;height:169px;border-radius:48px 48px 6px 6px;
  background:linear-gradient(180deg,#c9a88c 0,#d6b89e 30%,#b8cce3 46%,#a9c0dc 100%);
  -webkit-mask-image:linear-gradient(180deg,#000 80%,rgba(0,0,0,.6) 100%);
  mask-image:linear-gradient(180deg,#000 80%,rgba(0,0,0,.6) 100%)}
.owner-name{left:234px;top:31px;width:104px;text-align:center;font-family:"Libre Baskerville",serif;font-size:10px;line-height:12px;color:#243a5e}
.brand{left:380px;top:43px;font-size:14px;font-weight:700;color:var(--blue);white-space:nowrap}
.chat-tab{left:576px;top:0;width:136px;height:24px;background:var(--blue-deep);border-radius:0 0 14px 14px;color:#fff;font-size:10px;font-weight:700;display:flex;align-items:center;justify-content:center;gap:6px}
.chat-tab i{width:12px;height:9px;background:var(--yellow);border-radius:6px;display:block}
.phone{right:98px;top:31px;font-size:21px;font-weight:600;color:var(--blue-deep);white-space:nowrap}
.hours{right:98px;top:58px;text-align:right;font-size:10.5px;line-height:15.5px;color:#1b2c4a}
.social{right:98px;top:116px;display:flex;gap:3px}
.social span{width:15px;height:15px;border-radius:50%;background:var(--blue-deep)}
.tagline{right:96px;top:134px;font-size:10px;font-style:italic;font-weight:700;color:var(--blue-deep);letter-spacing:.5px}
/* nav */
.nav{left:100px;top:175px;width:600px;height:29px;background:#fff;display:flex;font-size:9px;border-bottom:1px solid #ddd}
.nav a{color:#333;text-decoration:none;padding:0 8px;display:flex;align-items:center;border-right:1px solid #ddd}
.nav a.active{background:var(--blue);color:#fff;padding:0 15px}
/* body panels */
.main{left:100px;top:204px;width:384px;height:787px;background:#fff}
.side{left:484px;top:204px;width:216px;height:787px;background:var(--side)}
.slider{left:108px;top:216px;width:369px;height:157px;background:linear-gradient(120deg,#a9b8cb 0,#6f8db8 35%,#2a5aa6 65%,#9fb3cc 100%)}
.slider-cap{left:108px;top:297px;width:186px;height:44px;background:var(--yellow);clip-path:polygon(0 0,100% 0,86% 100%,0 100%);padding:9px 0 0 16px;color:#fff;font-size:11px;line-height:12px}
.slider-cap small{display:block;color:#1b2c4a;font-size:8.5px;margin-top:3px}
.slider-arrows{left:458px;top:356px;width:19px;height:17px;background:rgba(0,0,0,.4);color:#fff;font-size:9px;text-align:center;line-height:17px}
.review{left:118px;width:340px}
.review .bubble{position:absolute;left:0;top:6px;width:24px;height:14px;border:1px solid #ccc;border-radius:50%;background:#fafafa}
.review .body{margin-left:30px}
.review .meta{display:flex;align-items:center;font-size:8px;color:var(--grey);height:12px}
.stars{color:var(--star);font-size:11px;letter-spacing:1px;margin-right:8px}
.meta em{flex:1}
.review p{font-size:7.3px;line-height:12.8px;color:var(--grey);margin-top:3px}
.review .ago{font-size:7.3px;color:var(--grey);margin-top:3px;display:flex;align-items:center;gap:6px}
.ago b{width:17px;height:17px;border-radius:2px;display:inline-block}
.services-title{left:128px;top:742px;font-size:14.5px;line-height:19.5px;color:#222;font-weight:400}
.services-intro{left:130px;top:787px;font-size:7px;color:var(--grey)}
.svc{top:806px;font-size:8px;line-height:14.6px;color:var(--blue-deep);list-style:none}
.svc li::before{content:"• ";color:var(--blue)}
.more{left:129px;top:904px;font-size:7.5px;font-weight:700;color:#111}
.badge{top:940px;height:36px;border-radius:4px}
/* sidebar */
.cta{left:491px;top:216px;width:194px;height:240px}
.cta-head{left:491px;top:224px;width:194px;text-align:center;color:#fff;font-size:8.5px}
.cta-head strong{display:block;font-size:15px;font-weight:600;margin-top:3px}
.cta-head strong span{color:var(--yellow)}
.btn-label{left:570px;color:#fff;font-size:7px;line-height:9px;text-align:center;width:70px}
.btn-label b{display:block;font-size:11px;font-weight:600;margin-top:1px}
.video{left:496px;top:487px;width:193px;height:127px;background:linear-gradient(110deg,#34466f 0,#506f9f 45%,#b0578a 75%,#a9bad2 100%)}
.blog-title{left:494px;top:647px;font-size:14.5px;color:var(--blue-deep);font-weight:400}
.post{left:496px;width:190px;height:50px}
.post .thumb{position:absolute;left:0;top:0;width:57px;height:48px;background:linear-gradient(135deg,#9cb0c8,#4d6a90 60%,#c9d2dc)}
.post .txt{position:absolute;left:64px;top:0;width:126px}
.post h4{font-size:8px;font-weight:400;color:var(--blue-deep)}
.post p{font-size:6.5px;line-height:11px;color:var(--blue);margin-top:2px}
.post a{display:block;font-size:6.5px;color:#222;margin-top:3px;text-decoration:none;font-weight:600}
/* footer */
.footer{left:100px;top:991px;width:600px;height:173px;background:linear-gradient(180deg,#1e63b9,#0d3f8b)}
.fcol{top:1010px;color:#fff}
.fcol h3{font-size:12px;font-weight:400;margin-bottom:6px}
.fcol li{list-style:none;font-size:7.5px;line-height:13.6px}
.fline{left:125px;top:1127px;width:558px;height:1px;background:rgba(255,255,255,.25)}
.copy{left:132px;top:1136px;font-size:7px;color:#c7d8f0}
</style>
</head>
<body>
<header>
  <div class="abs shop-photo" role="img" aria-label="Photo of the repair shop building"></div>
  <div class="abs owner-photo" role="img" aria-label="Portrait of owner Martin Kovacs"></div>
  <div class="abs owner-name">MARTIN KOVACS<br>OWNER</div>
  <div class="abs brand">Harbor Motor Repair</div>
  <div class="abs chat-tab"><i></i>Online Chat Now</div>
  <div class="abs phone">(480) 555-0142</div>
  <div class="abs hours">Hours: Mon-Fri 7am-6pm<br>2715 W. Alder Rd. #204<br>Tempe 85282</div>
  <div class="abs social"><span></span><span></span><span></span><span></span></div>
  <div class="abs tagline">Where People Count!</div>
</header>
<nav class="abs nav">
  <a class="active">Home</a><a>Stuff</a><a>Junk</a><a>Contact</a><a>About</a><a>Auto Repair</a><a>Loaner Cars</a><a>Free Shuttle Info</a><a>Win a Car</a><a>Germans</a><a style="border:0">Yes</a>
</nav>

<main>
  <div class="abs main"></div>
  <div class="abs slider" role="img" aria-label="Mechanic working under a car on a lift"></div>
  <div class="abs slider-cap">AUTO REPAIRING SERVICE<small>24/7 Customer Support</small></div>
  <div class="abs slider-arrows">‹ ›</div>

  <div class="abs review" style="top:396px"><div class="bubble"></div><div class="body">
    <div class="meta"><span class="stars">★★★★★</span><em>Dalena</em><span>July, 30 2013</span></div>
    <p>Etiam est nunc venenatis in tristique eu imperdiet ac nisl Cum sociis natoque penatibus et magnis dis parturient montes nascetur ridiculus mus In iaculis facilisis massa Etiam eu urna Sed porta Suspendisse quam leo molestie sed</p>
    <div class="ago">-322 days ago</div></div></div>

  <div class="abs review" style="top:487px"><div class="bubble"></div><div class="body">
    <div class="meta"><span class="stars">★★★★★</span><em>Dalena</em><span>July, 10 2013</span></div>
    <p>Etiam est nunc venenatis in tristique eu imperdiet ac nisl Cum sociis natoque penatibus et magnis dis parturient montes nascetur ridiculus mus In iaculis facilisis</p>
    <div class="ago">-322 days ago</div></div></div>

  <div class="abs review" style="top:569px"><div class="bubble"></div><div class="body">
    <div class="meta"><span class="stars">★★★★★</span><em>Dalena</em><span>July, 08 2013</span></div>
    <p>Etiam est nunc venenatis in tristique eu imperdiet ac nisl Cum sociis natoque penatibus et magnis dis parturient montes nascetur ridiculus mus In iaculis facilisis massa Etiam eu urna Sed porta Suspendisse quam leo molestie sed</p>
    <div class="ago">-322 days ago</div></div></div>

  <div class="abs review" style="top:661px"><div class="bubble"></div><div class="body">
    <div class="meta"><span class="stars">★★★★★</span><em>Dalena</em><span>July, 05 2013</span></div>
    <p>Etiam est nunc venenatis in tristique eu imperdiet ac nisl Cum sociis natoque penatibus et magnis dis parturient montes nascetur ridiculus mus In iaculis facilisis</p>
    <div class="ago">-322 days ago <b style="background:#c9302c"></b><b style="background:#d9473a"></b></div></div></div>

  <h1 class="abs services-title">Our Tempe Auto Repair Shop Offers<br>These Automotive Services:</h1>
  <div class="abs services-intro">Etiam est nunc venenatis in tristique eu imperdiet ac nisl Cum sociis natoque penatibus</div>
  <ul class="abs svc" style="left:130px">
    <li>Shuttle Service</li><li>General Auto Repair &amp; Maintenance</li><li>Transmission Repair &amp; Replacement</li><li>Manufacturer Recommended Service</li><li>Brake Repair and Replacement</li><li>Air Conditioning A/C Repair</li>
  </ul>
  <ul class="abs svc" style="left:300px">
    <li>Tire Repair and Replacement</li><li>Fuel System Repair</li><li>Exhaust System Repair</li><li>Engine Cooling System Maintenance</li><li>Electrical Diagnostics</li><li>Steering and Suspension Work</li>
  </ul>
  <div class="abs more">VIEW MORE &nbsp;SERVICES ›</div>
  <div class="abs badge" style="left:132px;width:96px;background:#ececec"></div>
  <div class="abs badge" style="left:255px;width:84px;background:#e8a324"></div>
  <div class="abs badge" style="left:366px;width:88px;background:#d6e2f2"></div>
</main>

<aside>
  <div class="abs side"></div>
  <svg class="abs cta" viewBox="0 0 194 240" width="194" height="240">
    <defs><linearGradient id="ctaBlue" x1="0" y1="0" x2="0" y2="1"><stop offset="0" stop-color="#3a86e4"/><stop offset="1" stop-color="#1552b5"/></linearGradient></defs>
    <path d="M0 0H194V220L97 240L0 220Z" fill="#fff"/>
    <path d="M0 0H194V44Q97 60 0 44Z" fill="url(#ctaBlue)"/>
    <path d="M0 192Q97 212 194 192V220L97 240L0 220Z" fill="url(#ctaBlue)"/>
    <path d="M58 72H170L182 88L170 104H58Z" fill="url(#ctaBlue)"/>
    <path d="M58 132H170L182 148L170 164H58Z" fill="url(#ctaBlue)"/>
    <circle cx="44" cy="88" r="26" fill="#dbe9fa"/><circle cx="44" cy="88" r="22" fill="url(#ctaBlue)"/>
    <circle cx="44" cy="148" r="26" fill="#dbe9fa"/><circle cx="44" cy="148" r="22" fill="url(#ctaBlue)"/>
    <path d="M32 92h24v6H32zM36 84l4-6h8l4 6z" fill="#fff"/>
    <circle cx="37" cy="99" r="3" fill="#fff"/><circle cx="51" cy="99" r="3" fill="#fff"/>
    <rect x="33" y="139" width="22" height="16" rx="2" fill="#fff"/><path d="M33 144h22" stroke="#1552b5" stroke-width="1.5"/>
  </svg>
  <div class="abs cta-head">Book Your Appointment Now and<strong>Get <span>$5</span> Discount!</strong></div>
  <div class="abs btn-label" style="top:296px">REQUEST A LONER<b>VEHICLE</b></div>
  <div class="abs btn-label" style="top:356px">MAKE AN<b>APPOINTMENT</b></div>

  <div class="abs video" role="img" aria-label="Video of the front counter with staff helping a customer"></div>
  <svg class="abs" style="left:578px;top:536px" width="28" height="28" viewBox="0 0 28 28"><circle cx="14" cy="14" r="12" fill="#111" stroke="#fff" stroke-width="2"/><path d="M11 8l9 6-9 6z" fill="#fff"/></svg>

  <h2 class="abs blog-title">Recent Blog Post</h2>
  <div class="abs post" style="top:675px"><div class="thumb" role="img" aria-label="Mechanic at work"></div><div class="txt"><h4>Etiam eu urna</h4><p>Sed porta Suspendisse quam leo molestie sed luctus quis feug</p><a>READ MORE</a></div></div>
  <div class="abs post" style="top:738px"><div class="thumb" role="img" aria-label="Technician in the shop"></div><div class="txt"><h4>Etiam eu urna</h4><p>Sed porta Suspendisse quam leo molestie sed luctus quis feug</p><a>READ MORE</a></div></div>
  <div class="abs post" style="top:801px"><div class="thumb" role="img" aria-label="Engine bay close-up"></div><div class="txt"><h4>Etiam eu urna</h4><p>Sed porta Suspendisse quam leo molestie sed luctus quis feug</p><a>READ MORE</a></div></div>
  <div class="abs post" style="top:864px"><div class="thumb" role="img" aria-label="Wheel and brake parts"></div><div class="txt"><h4>Etiam eu urna</h4><p>Sed porta Suspendisse quam leo molestie sed luctus quis feug</p><a>READ MORE</a></div></div>
</aside>

<footer>
  <div class="abs footer"></div>
  <div class="abs fcol" style="left:125px"><h3>Company</h3><ul><li>Etiam nunc venenatis</li><li>Yristique imperdiet</li><li>Cum sociis</li><li>Natoque penatibus</li><li>Dis parturient</li></ul></div>
  <div class="abs fcol" style="left:244px"><h3>Services</h3><ul><li>Etiam nunc venenatis</li><li>Yristique imperdiet</li><li>Cum sociis</li><li>Natoque penatibus</li><li>Dis parturient</li></ul></div>
  <div class="abs fcol" style="left:365px"><h3>Solutions</h3><ul><li>Etiam nunc venenatis</li><li>Yristique imperdiet</li><li>Cum sociis</li><li>Natoque penatibus</li><li>Dis parturient</li></ul></div>
  <div class="abs fcol" style="left:481px"><h3>Resources</h3><ul><li>Etiam nunc venenatis</li><li>Yristique imperdiet</li><li>Cum sociis</li><li>Natoque penatibus</li><li>Dis parturient</li></ul></div>
  <div class="abs fcol" style="left:592px"><h3>Contact Info</h3><ul><li>2715 W. Alder Rd. #204</li><li>Tempe, AZ 85282</li><li>(480) 555-0142</li><li>info@harbormotor.com</li></ul></div>
  <div class="abs fline"></div>
  <div class="abs copy">© 2013 Company Name. &nbsp;All right reserved. &nbsp;Term of Use</div>
</footer>
</body>
</html>
```